Business Card Design Project Calbrook Foundation

Looking for business card options to match our concurrent logo project on pixel forum. We are a international humanitarian aid firm. We work in the non profit sector but operate more closely to a traditional for-profit investment firm. As such we would like equal tones in our branding materials, which includes are business cards.

Stand by for logo...
Updates

logo uploaded.

Target Market(s)

Adults in western speaking countries ages 18-40 that work primarily in the NGO and Business Administrative Career Field.

Industry/Entity Type

Non Profit

Font styles to use
Sans Serif

Requirements
Nice to have
• We would like all contact information on one side.

Company Name/Logo, Individual Name and Position on the other...

```html
<!DOCTYPE html>
<html lang="en">
<head>
<meta charset="utf-8">
<title>Calbrook Foundation – Business Cards</title>
<link rel="stylesheet" href="https://fonts.googleapis.com/css2?family=Merriweather:wght@400;700&display=swap">
<style>
  :root {
    --page-bg: #d9d6d2;
    --card-bg: #333333;
    --logo-ink: #151515;
    --accent-blue: #3a9ad9;
    --text-light: #f2f2f2;
    --icon-blue: #3a9ad9;
    --divider: #8a8a8a;
  }
  * { margin: 0; padding: 0; box-sizing: border-box; }
  html, body {
    width: 1200px; height: 873px; overflow: hidden;
    background: var(--page-bg);
    font-family: "Merriweather", Georgia, serif;
  }
  .canvas {
    position: relative; width: 1200px; height: 873px;
    display: flex; align-items: center; justify-content: center; gap: 60px;
  }
  .card {
    position: relative;
    width: 520px; height: 297px;
    background: var(--card-bg);
    border-radius: 3px;
    box-shadow: 0 10px 24px rgba(0,0,0,0.25);
  }
  .brand {
    display: flex; align-items: center; gap: 10px;
    color: var(--logo-ink);
    font-weight: 700;
    letter-spacing: 0.02em;
    white-space: nowrap;
  }
  .brand-mark {
    width: 14px; height: 14px; border-radius: 50%;
    background: var(--logo-ink);
    flex: none;
  }
  .card--contact .brand {
    position: absolute; left: 28px; top: 50%;
    transform: translateY(-50%);
    font-size: 17px;
  }
  .card--contact .divider {
    position: absolute; left: 280px; top: 40px; bottom: 40px; width: 1px;
    background: linear-gradient(to bottom, transparent, var(--divider) 50%, transparent);
  }
  .contact {
    position: absolute; left: 302px; top: 50%;
    transform: translateY(-50%);
    color: var(--text-light);
  }
  .contact-name {
    color: var(--accent-blue);
    font-size: 14px; font-weight: 700; letter-spacing: 0.04em;
    text-transform: uppercase;
  }
  .contact-role { font-size: 12px; margin: 4px 0 14px; }
  .contact-list { list-style: none; font-size: 12px; }
  .contact-list li {
    display: flex; align-items: center; gap: 9px;
    margin-bottom: 7px;
    white-space: nowrap;
  }
  .contact-icon { width: 11px; height: 11px; flex: none; }
  .contact-icon svg { display: block; width: 11px; height: 11px; }
  .card--logo { display: flex; align-items: center; justify-content: center; }
  .card--logo .brand { font-size: 26px; gap: 14px; }
  .card--logo .brand-mark { width: 20px; height: 20px; }
</style>
</head>
<body>
<main class="canvas">
  <section class="card card--contact" aria-label="Business card, contact side">
    <div class="brand"><span class="brand-mark"></span>Calbrook Foundation</div>
    <div class="divider"></div>
    <div class="contact">
      <p class="contact-name">Aaron Hale</p>
      <p class="contact-role">Managing Director</p>
      <ul class="contact-list">
        <li>
          <span class="contact-icon">
            <svg viewBox="0 0 12 12"><rect x="3" y="1" width="6" height="10" rx="1" fill="none" stroke="var(--icon-blue)" stroke-width="1.2"/></svg>
          </span>+101 555 0142
        </li>
        <li>
          <span class="contact-icon">
            <svg viewBox="0 0 12 12"><rect x="1" y="2.5" width="10" height="7" fill="var(--icon-blue)"/><path d="M1 2.5 L6 6.5 L11 2.5" fill="none" stroke="var(--card-bg)" stroke-width="0.9"/></svg>
          </span>aaronhale@example.com
        </li>
        <li>
          <span class="contact-icon">
            <svg viewBox="0 0 12 12"><circle cx="6" cy="6" r="5" fill="none" stroke="var(--icon-blue)" stroke-width="1.1"/><path d="M1 6 H11 M6 1 C3.5 3.5 3.5 8.5 6 11 M6 1 C8.5 3.5 8.5 8.5 6 11" fill="none" stroke="var(--icon-blue)" stroke-width="0.9"/></svg>
          </span>www.calbrook.org
        </li>
        <li>
          <span class="contact-icon">
            <svg viewBox="0 0 12 12"><circle cx="6" cy="6" r="4.5" fill="var(--icon-blue)"/></svg>
          </span>www.socialpost.net
        </li>
        <li>
          <span class="contact-icon">
            <svg viewBox="0 0 12 12"><circle cx="6" cy="6" r="4.5" fill="var(--icon-blue)"/></svg>
          </span>www.friendpage.net
        </li>
      </ul>
    </div>
  </section>

  <section class="card card--logo" aria-label="Business card, logo side">
    <div class="brand"><span class="brand-mark"></span>Calbrook Foundation</div>
  </section>
</main>
</body>
</html>
```